KAVELUXE Consultancy Business Card

We need a business card design for a new Image & Etiquette Consultancy Company.

The design should reflect the corporate colour found in the logo attached.

Info to include:

Name: Marelda Quon
Title: Image Consultant
Company: KA VELUXE CONSULTANCY
Address: 27 Pelham Street, #14-08 Harbourview Tower, Singapore 048215
Contact: 9317 6408
Email: marelda@kaveluxe.com.sg
Website: www.kaveluxe.com.sg

Industry/Entity Type

Business

```html
<!DOCTYPE html>
<html lang="en">
<head>
<meta charset="utf-8">
<title>KA VELUXE Consultancy – Business Card</title>
<link href="https://fonts.googleapis.com/css2?family=Montserrat:wght@500;700&display=swap" rel="stylesheet">
<style>
  :root {
    --backdrop: #e8e6eb;
    --card-white: #ffffff;
    --plum: #2f0f47;
    --plum-ink: #3b1a55;
    --gold: #e0ad3a;
    --gold-light: #f5d684;
    --gold-deep: #c18d22;
    --text-light: #ffffff;
  }
  * { box-sizing: border-box; margin: 0; padding: 0; }
  html, body {
    width: 1200px; height: 632px; overflow: hidden;
    background: var(--backdrop);
    font-family: "Montserrat", Arial, sans-serif;
  }
  .canvas { position: relative; width: 1200px; height: 632px; }

  .card {
    position: absolute; top: 160px;
    width: 530px; height: 312px;
    border-radius: 24px;
    box-shadow: 0 10px 28px rgba(40, 20, 60, 0.18);
    overflow: hidden;
  }

  /* Front */
  .card-front { left: 50px; background: var(--card-white); }
  .front-brand {
    position: absolute; left: 0; right: 0; top: 92px;
    text-align: center;
    font-weight: 500; font-size: 50px; letter-spacing: 3px;
    color: var(--plum-ink);
  }
  .front-band {
    position: absolute; left: 0; right: 0; top: 198px; height: 42px;
    background: linear-gradient(180deg, var(--gold-light) 0%, var(--gold) 45%, var(--gold-deep) 100%);
    display: flex; align-items: center; justify-content: center;
    font-weight: 700; font-size: 13px; letter-spacing: 2.6px;
    color: var(--plum);
  }

  /* Back */
  .card-back { left: 620px; background: var(--plum); color: var(--text-light); }
  .back-brand {
    position: absolute; right: 34px; top: 38px;
    font-weight: 500; font-size: 34px; letter-spacing: 2px;
    color: var(--gold);
  }
  .company {
    position: absolute; left: 34px; top: 44px;
    font-weight: 700; font-size: 12px; letter-spacing: 2.4px;
    color: var(--gold);
  }
  .address {
    position: absolute; left: 34px; top: 72px;
    font-weight: 700; font-size: 11px; letter-spacing: 2px; line-height: 18px;
    font-style: normal;
  }
  .person { position: absolute; right: 34px; top: 150px; text-align: right; }
  .person-name {
    font-weight: 700; font-size: 13px; letter-spacing: 2.6px; color: var(--gold);
  }
  .person-title {
    margin-top: 6px;
    font-weight: 700; font-size: 13px; letter-spacing: 2.6px;
  }
  .contacts { position: absolute; right: 34px; top: 216px; list-style: none; }
  .contacts li {
    display: flex; align-items: center; justify-content: flex-end; gap: 8px;
    height: 22px;
    font-weight: 500; font-size: 11px; letter-spacing: 1.6px;
  }
  .contacts svg { width: 16px; height: 16px; }
</style>
</head>
<body>
<main class="canvas">

  <section class="card card-front" aria-label="Card front">
    <div class="front-brand">KA VELUXE</div>
    <div class="front-band">IMAGE &amp; ETIQUETTE CONSULTANCY COMPANY</div>
  </section>

  <section class="card card-back" aria-label="Card back">
    <div class="back-brand">KA VELUXE</div>
    <div class="company">KA VELUXE CONSULTANCY</div>
    <address class="address">
      27 PELHAM STREET, #14-08<br>
      HARBOURVIEW TOWER<br>
      SINGAPORE 048215
    </address>

    <div class="person">
      <div class="person-name">MARELDA QUON</div>
      <div class="person-title">IMAGE CONSULTANT</div>
    </div>

    <ul class="contacts">
      <li>9317 6408
        <svg viewBox="0 0 16 16" aria-hidden="true">
          <rect width="16" height="16" rx="2" fill="var(--gold)"/>
          <rect x="5" y="2.5" width="6" height="11" rx="1" fill="none" stroke="var(--plum)" stroke-width="1.2"/>
          <circle cx="8" cy="11.5" r="0.7" fill="var(--plum)"/>
        </svg>
      </li>
      <li>marelda@kaveluxe.com.sg
        <svg viewBox="0 0 16 16" aria-hidden="true">
          <rect width="16" height="16" rx="2" fill="var(--gold)"/>
          <rect x="3" y="4.5" width="10" height="7" fill="none" stroke="var(--plum)" stroke-width="1.2"/>
          <path d="M3 4.5 L8 8.5 L13 4.5" fill="none" stroke="var(--plum)" stroke-width="1.2"/>
        </svg>
      </li>
      <li>www.kaveluxe.com.sg
        <svg viewBox="0 0 16 16" aria-hidden="true">
          <rect width="16" height="16" rx="2" fill="var(--gold)"/>
          <circle cx="8" cy="8" r="4.8" fill="none" stroke="var(--plum)" stroke-width="1.2"/>
          <ellipse cx="8" cy="8" rx="2" ry="4.8" fill="none" stroke="var(--plum)" stroke-width="1"/>
          <line x1="3.2" y1="8" x2="12.8" y2="8" stroke="var(--plum)" stroke-width="1"/>
        </svg>
      </li>
    </ul>
  </section>

</main>
</body>
</html>
```